Double caffeinated coffee label design

We need to design labels for a new coffee brand. The label size: 2.75” x 4.125” (Corners slightly rounded). There will be front and back label in stickers to be put on standardized bags. Our product is roasted whole bean and ground coffee in 12oz bags. It is described as "strong, bold, intense, and double caffeinated. The product is designed for passionate coffee drinkers who want strong, more caffeinated but not bitter coffee. The coffee is suitable for espresso base coffees.
Target Market(s)
Groceries, food stores, super markets. Heavy and sophisticated coffee drinkers.
Requirements
Must have
- Modern, minimalist style. Strong and bold look. Creative. Impressive.
Nice to have
- Some impressed coffee label designs for reference: https://www.trevalo.net/find?q=most+impressive+coffee+brand+designs&from=qwer&kind=pics&sa=Y&ref=7bZkQxmPtLrsWvNcYhDjKeFgAoUiBnMwZpRsTeQvLbXy_KHJaPqWz&vw=1280&vh=610#pic=kR4mTzWqPxNbLo:

```html
<!DOCTYPE html>
<html lang="en">
<head>
<meta charset="utf-8">
<title>Valoro – Roasted Whole Bean Coffee Labels</title>
<link rel="stylesheet" href="https://fonts.googleapis.com/css2?family=Roboto+Condensed:wght@700&display=swap">
<style>
  :root {
    --backdrop: #212121;
    --orange: #e07a30;
    --orange-deep: #b9541a;
    --black: #0d0d0d;
    --band-dark: #272727;
    --white: #ffffff;
  }
  * { margin: 0; padding: 0; box-sizing: border-box; }
  html, body {
    width: 1200px;
    height: 1200px;
    overflow: hidden;
    background: var(--backdrop);
  }
  .canvas {
    position: relative;
    width: 1200px;
    height: 1200px;
    font-family: "Roboto Condensed", "Arial Narrow", sans-serif;
    font-weight: 700;
  }
  .label {
    position: absolute;
    top: 328px;
    width: 253px;
    height: 658px;
    overflow: hidden;
  }
  .label--classic { left: 286px; background: var(--black); color: var(--orange); }
  .label--inverse { left: 655px; background: var(--orange); color: var(--black); }

  .label__top {
    height: 118px;
  }
  .label--classic .label__top { background: var(--orange); }
  .label--inverse .label__top { background: var(--black); }

  .brand {
    position: absolute;
    top: 152px;
    left: 0;
    width: 100%;
    text-align: center;
    font-size: 40px;
    letter-spacing: 1px;
    line-height: 1;
  }
  .label--classic .brand { color: var(--white); }
  .label--inverse .brand { color: var(--black); }

  .product {
    position: absolute;
    left: 63px;
    line-height: 1;
    text-transform: uppercase;
  }
  .product--roasted { top: 596px; top: 268px; font-size: 39px; }
  .product--whole { top: 313px; font-size: 26px; }

  .coffee-band {
    position: absolute;
    top: 344px;
    left: 22px;
    right: 0;
    height: 72px;
    display: flex;
    align-items: center;
    padding-left: 41px;
    font-size: 46px;
    line-height: 1;
  }
  .label--classic .coffee-band { background: var(--band-dark); }
  .label--inverse .coffee-band { background: var(--orange-deep); }

  .ornament {
    position: absolute;
    left: 0;
    right: 0;
    bottom: 0;
    height: 242px;
  }
  .label--classic .ornament {
    background: linear-gradient(160deg, var(--black) 0%, var(--orange) 55%, var(--black) 100%);
  }
  .label--inverse .ornament {
    background: linear-gradient(160deg, var(--orange) 0%, var(--black) 55%, var(--orange) 100%);
  }
</style>
</head>
<body>
<main class="canvas">

  <section class="label label--classic">
    <div class="label__top"></div>
    <div class="brand">VALORO</div>
    <div class="product product--roasted">Roasted</div>
    <div class="product product--whole">Whole Bean</div>
    <div class="coffee-band">COFFEE</div>
    <div class="ornament" role="img" aria-label="Large orange swirl ornament rising from the bottom of the label"></div>
  </section>

  <section class="label label--inverse">
    <div class="label__top"></div>
    <div class="brand">VALORO</div>
    <div class="product product--roasted">Roasted</div>
    <div class="product product--whole">Whole Bean</div>
    <div class="coffee-band">COFFEE</div>
    <div class="ornament" role="img" aria-label="Large black swirl ornament rising from the bottom of the label"></div>
  </section>

</main>
</body>
</html>
```